Business card design only (Have Logo Online) Shoudl be quick and easy for designer

We would like to have a business card design that is in-line with our company logo. Final deliverables should include two EPS extension file. One for the front card design and the other the back-end design. Please also indicate the font style used.

Advisory Pebbles is a social enterprise that focuses on utilizing technology, unique methodologies and international partnerships to provide a one-stop location for economical and dependable IT-related solutions.

Target Market(s)

Micro, small and medium business owners.

Industry/Entity Type

Business

Requirements
Must have
• The business card should incorporate our company logo.
Nice to have
• A little web 2.0 style would be nice but I haven''t decided yet.

```html
<!DOCTYPE html>
<html lang="en">
<head>
<meta charset="utf-8">
<title>Advisory Pebbles – Business Card Set</title>
<link rel="stylesheet" href="https://fonts.googleapis.com/css2?family=Source+Sans+3:ital,wght@0,400;0,700;1,400&family=Dancing+Script:wght@500&display=swap">
<style>
  :root {
    --page: #ffffff;
    --ink: #1a1a1a;
    --brand-green: #3fae2a;
    --name-green: #46b02e;
    --mint-soft: #e8f9dc;
    --mint-band: #c9fd97;
    --aqua-soft: #e6fbf3;
    --aqua-band: #c6ffe2;
    --cream-soft: #f7f6e2;
    --lemon-band: #f6f46c;
    --back-green-soft: #effce6;
    --ring-faint: #d9f9b8;
    --card-shadow: rgba(0, 0, 0, 0.45);
  }
  * { margin: 0; padding: 0; box-sizing: border-box; }
  html, body { width: 1200px; height: 1055px; overflow: hidden; background: var(--page); }
  .sheet { position: relative; width: 1200px; height: 1055px; }

  .card {
    position: absolute;
    width: 552px;
    height: 315px;
    overflow: hidden;
    box-shadow: 2px 2px 2px var(--card-shadow);
    font-family: "Source Sans 3", Arial, sans-serif;
    color: var(--ink);
  }
  .col-left  { left: 38px; }
  .col-right { left: 613px; }
  .row-1 { top: 25px; }
  .row-2 { top: 366px; }
  .row-3 { top: 709px; }

  /* Front cards */
  .front .band { position: absolute; top: 0; right: 0; width: 37%; height: 100%; }
  .front.theme-mint  { background: var(--mint-soft); }
  .front.theme-mint .band  { background: var(--mint-band); }
  .front.theme-aqua  { background: var(--aqua-soft); }
  .front.theme-aqua .band  { background: var(--aqua-band); }
  .front.theme-lemon { background: var(--cream-soft); }
  .front.theme-lemon .band { background: var(--lemon-band); }

  .brand {
    position: absolute;
    left: 0; right: 0;
    top: 182px;
    display: flex;
    align-items: center;
    justify-content: center;
    gap: 14px;
  }
  .brand-dot {
    width: 34px; height: 34px;
    border-radius: 50%;
    background: var(--brand-green);
  }
  .brand-name {
    font-weight: 700;
    font-size: 46px;
    letter-spacing: 1px;
    color: var(--brand-green);
    line-height: 1;
  }

  .tagline {
    position: absolute;
    font-family: "Dancing Script", cursive;
    font-weight: 500;
    color: var(--ink);
    white-space: nowrap;
  }
  .tagline-bottom { left: 0; right: 0; text-align: center; top: 252px; font-size: 24px; }
  .tagline-top { right: 14px; top: 10px; font-size: 30px; }

  /* Back cards */
  .back.theme-green { background: linear-gradient(90deg, var(--back-green-soft), #f3fde9); }
  .back.theme-cream { background: var(--cream-soft); }
  .back .backdrop { position: absolute; left: 0; top: 0; width: 300px; height: 315px; }

  .contact {
    position: absolute;
    right: 22px;
    top: 22px;
    text-align: right;
  }
  .person-header { display: inline-block; text-align: center; }
  .person-name {
    font-weight: 700;
    font-size: 30px;
    line-height: 1;
    color: var(--name-green);
  }
  .person-role {
    font-style: italic;
    font-size: 18px;
    margin-top: 2px;
  }
  .address { margin-top: 20px; font-size: 22px; line-height: 29px; }
  .lines { margin-top: 22px; font-size: 21px; line-height: 27px; }
</style>
</head>
<body>
<main class="sheet">

  <!-- Front, mint -->
  <section class="card front theme-mint col-left row-1">
    <div class="band"></div>
    <div class="brand"><span class="brand-dot"></span><span class="brand-name">Advisory Pebbles</span></div>
    <p class="tagline tagline-bottom">Delivering affordable, simple and innovative results!</p>
  </section>

  <!-- Front, mint with slogan -->
  <section class="card front theme-mint col-right row-1">
    <div class="band"></div>
    <p class="tagline tagline-top">Growing with you!</p>
    <div class="brand"><span class="brand-dot"></span><span class="brand-name">Advisory Pebbles</span></div>
  </section>

  <!-- Back, green -->
  <section class="card back theme-green col-left row-2">
    <svg class="backdrop" viewBox="0 0 300 315" role="img" aria-label="Soft pale green circular backdrop">
      <circle cx="90" cy="180" r="210" fill="var(--ring-faint)" opacity="0.6"/>
      <circle cx="70" cy="170" r="180" fill="var(--back-green-soft)"/>
    </svg>
    <div class="contact">
      <div class="person-header">
        <h1 class="person-name">Marlen Okafor</h1>
        <p class="person-role">Founder</p>
      </div>
      <p class="address">2148 Alder Lane<br>BC Canada<br>V6K 2J9</p>
      <p class="lines">Cell: 1-604-555-0148<br>E-mail: marlen.okafor@advisorypebbles.com<br>www.advisorypebbles.com</p>
    </div>
  </section>

  <!-- Front, aqua -->
  <section class="card front theme-aqua col-right row-2">
    <div class="band"></div>
    <div class="brand"><span class="brand-dot"></span><span class="brand-name">Advisory Pebbles</span></div>
    <p class="tagline tagline-bottom">Delivering affordable, simple and innovative results!</p>
  </section>

  <!-- Back, cream -->
  <section class="card back theme-cream col-left row-3">
    <svg class="backdrop" viewBox="0 0 300 315" role="img" aria-label="Soft pale green circular backdrop">
      <circle cx="90" cy="180" r="210" fill="var(--ring-faint)" opacity="0.7"/>
      <circle cx="70" cy="170" r="180" fill="var(--cream-soft)"/>
    </svg>
    <div class="contact">
      <div class="person-header">
        <h1 class="person-name">Marlen Okafor</h1>
        <p class="person-role">Founder</p>
      </div>
      <p class="address">2148 Alder Lane<br>BC Canada<br>V6K 2J9</p>
      <p class="lines">Cell: 1-604-555-0148<br>E-mail: marlen.okafor@advisorypebbles.com<br>www.advisorypebbles.com</p>
    </div>
  </section>

  <!-- Front, lemon with slogan -->
  <section class="card front theme-lemon col-right row-3">
    <div class="band"></div>
    <p class="tagline tagline-top">Growing with you!</p>
    <div class="brand"><span class="brand-dot"></span><span class="brand-name">Advisory Pebbles</span></div>
  </section>

</main>
</body>
</html>
```